Tallowreed Advisory Partners Business Card Design

We have the logo we just need someone to design a modern business card design.

Name: Desmond Munkalt
Phone: 3055550148
Mobile: 9175550193
Web:www.tallowreedadvisory.example
email: dmunkalt@tallowreedadvisory.example
Company: Tallowreed Advisory Partners
Title: CEO

Address: 718 Quillmore Ave, Miami, Florida 33190

Target Market(s)

companies over 100 employees

Industry/Entity Type

Business

```html
<!DOCTYPE html>
<html lang="en">
<head>
<meta charset="utf-8">
<title>Tallowreed Advisory Partners — Business Card</title>
<link rel="stylesheet" href="https://fonts.googleapis.com/css2?family=Open+Sans:wght@400;600;700&display=swap">
<style>
  :root {
    --brand-blue: #0a5cf5;
    --brand-blue-deep: #0843c4;
    --brand-blue-glow: #1f6cf7;
    --ink: #111111;
    --ink-soft: #2b2b2b;
    --paper: #ffffff;
    --page-top: #ffffff;
    --page-bottom: #ebebeb;
    --rule: #d6d6d6;
  }
  * { margin: 0; padding: 0; box-sizing: border-box; }
  html, body { width: 1200px; height: 900px; overflow: hidden; }
  body {
    position: relative;
    font-family: "Open Sans", Arial, sans-serif;
    background: linear-gradient(to bottom, var(--page-top) 0%, var(--page-top) 35%, var(--page-bottom) 100%);
    color: var(--ink);
  }

  /* Logo lockup on the presentation */
  .brand-lockup {
    position: absolute;
    left: 0; width: 1200px; top: 156px;
    display: flex; flex-direction: column; align-items: center;
  }
  .brand-lockup .brand-mark { width: 92px; height: 92px; border-radius: 50%; background: var(--brand-blue); }
  .brand-lockup .brand-name {
    margin-top: 14px;
    font-weight: 700; font-size: 28px; letter-spacing: 1px;
    line-height: 1.15; text-align: center; text-transform: uppercase;
    color: var(--ink);
  }

  /* Cards */
  .card {
    position: absolute; top: 399px;
    width: 463px; height: 284px;
    overflow: hidden;
  }
  .card-front {
    left: 129px;
    background: radial-gradient(ellipse 60% 65% at 50% 45%, var(--brand-blue-glow) 0%, var(--brand-blue) 45%, var(--brand-blue-deep) 100%);
    display: flex; flex-direction: column; align-items: center; justify-content: center;
  }
  .card-front .brand-mark { width: 74px; height: 74px; border-radius: 50%; background: var(--paper); }
  .card-front .brand-name {
    margin-top: 10px;
    font-weight: 700; font-size: 20px; letter-spacing: 0.8px;
    line-height: 1.15; text-align: center; text-transform: uppercase;
    color: var(--paper);
  }

  .card-back { left: 621px; background: var(--paper); }
  .card-back .back-logo {
    position: absolute; left: 20px; top: 70px; width: 170px;
    display: flex; flex-direction: column; align-items: center;
  }
  .card-back .brand-mark { width: 56px; height: 56px; border-radius: 50%; background: var(--brand-blue); }
  .card-back .brand-name {
    margin-top: 8px;
    font-weight: 700; font-size: 14px; letter-spacing: 0.5px;
    line-height: 1.15; text-align: center; text-transform: uppercase;
    color: var(--ink);
  }
  .holder {
    position: absolute; right: 27px; top: 64px;
    text-align: right;
  }
  .holder-name {
    display: inline-block;
    font-size: 23px; font-weight: 400; color: var(--brand-blue);
    padding-bottom: 2px; border-bottom: 1px solid var(--rule);
  }
  .contact-list {
    list-style: none; margin-top: 22px;
    font-size: 13px; line-height: 18px; color: var(--ink-soft);
  }
  .card-back .card-band {
    position: absolute; left: 0; right: 0; bottom: 0; height: 15px;
    background: var(--brand-blue);
  }

  .page-band {
    position: absolute; left: 0; right: 0; bottom: 0; height: 19px;
    background: var(--brand-blue);
  }
</style>
</head>
<body>
  <header class="brand-lockup">
    <div class="brand-mark"></div>
    <div class="brand-name">Tallowreed<br>Advisory Partners</div>
  </header>

  <section class="card card-front" aria-label="Card front">
    <div class="brand-mark"></div>
    <div class="brand-name">Tallowreed<br>Advisory Partners</div>
  </section>

  <section class="card card-back" aria-label="Card back">
    <div class="back-logo">
      <div class="brand-mark"></div>
      <div class="brand-name">Tallowreed<br>Advisory Partners</div>
    </div>
    <div class="holder">
      <h1 class="holder-name">Desmond Munkalt</h1>
      <ul class="contact-list">
        <li>Phone: 3055550148</li>
        <li>Mobile: 9175550193</li>
        <li>Web:www.tallowreedadvisory.example</li>
        <li>email: dmunkalt@tallowreedadvisory.example</li>
        <li>Company: Tallowreed Advisory Partners</li>
        <li>Title: CEO</li>
      </ul>
    </div>
    <div class="card-band"></div>
  </section>

  <div class="page-band"></div>
</body>
</html>
```